Quillbrook Pharma Business Card

Quillbrook Pharma in the upper left hand corner with the following underneath

Validated ERP Software
Pharma | Medical Devices | Contract Manufacturing

phone (555) 482-7316 x184

fax (555) 937-0658

email dvoss@quillbrooksystems.example

web www.quillbrooksystems.example

Boston | Sarasota | St Petersburg

```html
<!DOCTYPE html>
<html lang="en">
<head>
<meta charset="utf-8">
<title>Quillbrook Pharma Business Card</title>
<link href="https://fonts.googleapis.com/css2?family=Open+Sans:wght@400;700;800&display=swap" rel="stylesheet">
<style>
  :root {
    --bg: #8c8c8c;
    --card: #1b1b1b;
    --green: #8dc63f;
    --blue: #1f5fae;
    --white: #f2f2f2;
  }
  * { margin: 0; padding: 0; box-sizing: border-box; }
  html, body { width: 1200px; height: 960px; overflow: hidden; }
  body {
    background: var(--bg);
    font-family: "Open Sans", sans-serif;
    position: relative;
  }
  .card {
    position: absolute;
    width: 700px;
    height: 400px;
    background: var(--card);
    border-radius: 28px;
  }
  .card--front { left: 110px; top: 60px; }
  .card--back { left: 390px; top: 500px; }

  .brand {
    display: flex;
    align-items: center;
    gap: 18px;
  }
  .brand__dot {
    flex: none;
    border-radius: 50%;
    background: var(--blue);
  }
  .brand__name {
    color: var(--green);
    font-weight: 800;
    letter-spacing: 0.5px;
    white-space: nowrap;
  }

  .card--front .brand {
    position: absolute;
    left: 0; right: 0; top: 0; bottom: 0;
    justify-content: center;
  }
  .card--front .brand__dot { width: 44px; height: 44px; }
  .card--front .brand__name { font-size: 60px; }

  .card--back {
    display: flex;
    flex-direction: column;
    align-items: center;
    padding-top: 40px;
    text-align: center;
  }
  .card--back .brand__dot { width: 30px; height: 30px; }
  .card--back .brand__name { font-size: 44px; }

  .tagline {
    margin-top: 22px;
    color: var(--green);
    font-weight: 700;
    font-size: 30px;
    line-height: 1.1;
  }
  .sectors {
    margin-top: 6px;
    color: var(--white);
    font-size: 17px;
  }
  .contact-icons {
    margin-top: 18px;
    display: flex;
    gap: 10px;
  }
  .contact-icons svg { width: 18px; height: 18px; display: block; }
  .contact-list {
    margin-top: 8px;
    list-style: none;
    color: var(--white);
    font-size: 19px;
    line-height: 1.35;
  }
</style>
</head>
<body>
  <section class="card card--front" aria-label="Card front">
    <div class="brand">
      <span class="brand__dot"></span>
      <span class="brand__name">Quillbrook Pharma</span>
    </div>
  </section>

  <section class="card card--back" aria-label="Card back">
    <div class="brand">
      <span class="brand__dot"></span>
      <span class="brand__name">Quillbrook Pharma</span>
    </div>
    <p class="tagline">Validated ERP Software</p>
    <p class="sectors">Pharma | Medical Devices | Contract Manufacturing</p>
    <div class="contact-icons" aria-hidden="true">
      <svg viewBox="0 0 20 20"><circle cx="10" cy="10" r="9" fill="var(--green)"/><path d="M6 6.5c0 4 3.5 7.5 7.5 7.5l1-2-2.2-1-1 1c-1.3-.6-2.2-1.5-2.8-2.8l1-1-1-2.2z" fill="var(--card)"/></svg>
      <svg viewBox="0 0 20 20"><rect x="4" y="2" width="9" height="5" fill="var(--green)"/><rect x="2" y="7" width="16" height="11" rx="1.5" fill="var(--green)"/><rect x="5" y="10" width="2" height="2" fill="var(--card)"/><rect x="9" y="10" width="2" height="2" fill="var(--card)"/><rect x="13" y="10" width="2" height="2" fill="var(--card)"/><rect x="5" y="14" width="10" height="2" fill="var(--card)"/></svg>
      <svg viewBox="0 0 20 20"><rect x="1" y="4" width="18" height="12" rx="1.5" fill="var(--green)"/><path d="M2 5l8 6 8-6" stroke="var(--card)" stroke-width="1.6" fill="none"/></svg>
      <svg viewBox="0 0 20 20"><circle cx="10" cy="10" r="9" fill="var(--green)"/><path d="M1 10h18M10 1c-3 3-3 15 0 18M10 1c3 3 3 15 0 18" stroke="var(--card)" stroke-width="1.4" fill="none"/></svg>
    </div>
    <ul class="contact-list">
      <li>(555) 482-7316 x184</li>
      <li>(555) 937-0658</li>
      <li>dvoss@quillbrooksystems.example</li>
      <li>www.quillbrooksystems.example</li>
    </ul>
  </section>
</body>
</html>
```